Fresh, modern brand required for new start-up!

TallCropNear is a new venture offering an end-to-end communications and media relations service including strategy development, execution and evaluation; copy writing and editing; social and e- media management; leadership coaching, media training and more.

I require a fresh and lively corporate identity to mirror the ethos of the business.

I need a logo, business card (double-sided preferably), letterhead (for invoicing and client communications) and compliment slip. As a start-up, budget will be an ongoing consideration for me so, ideally, I would prefer a two-colour logo - although if you wow me with something more than that, I may have to throw caution to the wind!

The ethos behind my name is twofold; one, I have moved from being something of a "big fish in a small pond" (a director in a single company) to a small fish in the big pond of small businesses. Two, I may be a "small fish", but that doesn't mean I don't "fish big".

I am looking for a clean, simple design that will look good on a variety of mediums, big or small. The design should be young and fresh and make an immediate impact. I want the design to reflect the fact that I specialise in tailored, simple and effective communications.

Target Market(s)

My clients range from global financial services, resources and technology companies to not-for-profit organisations and other small businesses. Moreover, my current client base stretches from Asia Pacific (incl. Australia), to Europe (incl. UK) and the US. All my clients speak English (even if as a second language) and are relatively senior communications professionals within their organisations.

Industry/Entity Type

Communications

Requirements
Nice to have
• The design/logo could include symbols and/or characters that double as imagery. For example: an upside down question mark (?) might look like a fishing line/hook and a flattened @ sign, might look like a pond...
Should not have
• The design should not use old-style serif fonts, but nor should it be "cartoony" in any way. No navy blue, grey or sombre corporate colours.

```html
<!DOCTYPE html>
<html lang="en">
<head>
<meta charset="utf-8">
<title>TallCropNear – Stationery Set</title>
<link href="https://fonts.googleapis.com/css2?family=Yanone+Kaffeesatz:wght@200;300;400;700&display=swap" rel="stylesheet">
<style>
  :root {
    --ink: #1c1c1c;
    --teal: #0e7c5f;
    --leaf: #7ac143;
    --lime: #b8e61c;
    --pale-green: #8fc66a;
    --sheet: #ffffff;
    --edge: #9a9a9a;
    --page: #ffffff;
  }
  * { margin: 0; padding: 0; box-sizing: border-box; }
  html, body { width: 1200px; height: 900px; overflow: hidden; background: var(--page); }
  body { position: relative; font-family: "Yanone Kaffeesatz", "Arial Narrow", sans-serif; color: var(--ink); }

  .sheet { position: absolute; background: var(--sheet); border: 1px solid var(--edge); }
  .abs { position: absolute; }

  .brand-dot { position: absolute; border-radius: 50%; background: var(--leaf); }
  .brand-name { position: absolute; font-weight: 400; color: var(--ink); white-space: nowrap; line-height: 1; }
  .tagline { position: absolute; font-weight: 200; color: var(--pale-green); white-space: nowrap; line-height: 1; }

  .contact { position: absolute; color: var(--teal); font-weight: 300; line-height: 1.45; white-space: nowrap; }
  .contact .light { color: var(--pale-green); }
  .contact strong { font-weight: 400; }

  /* Primary logo */
  .logo-main .brand-dot { left: 50px; top: 100px; width: 80px; height: 80px; }
  .logo-main .brand-name { left: 28px; top: 194px; font-size: 32px; }
  .logo-main .tagline { left: 28px; top: 229px; font-size: 11px; }

  /* Business card front */
  .card-front { left: 214px; top: 119px; width: 208px; height: 116px; }
  .card-front .brand-dot { left: 42px; top: 16px; width: 48px; height: 48px; }
  .card-front .brand-name { left: 20px; top: 78px; font-size: 17px; }
  .card-front .tagline { left: 20px; top: 98px; font-size: 5.5px; }
  .card-front .holder { position: absolute; left: 135px; top: 38px; font-size: 7px; font-weight: 400; }
  .card-front .contact { left: 135px; top: 50px; font-size: 5px; }

  /* Business card back */
  .card-back { left: 441px; top: 119px; width: 208px; height: 116px; border-color: #b9c9a9;
    background: linear-gradient(180deg, var(--lime) 0%, #5cbf2a 50%, var(--teal) 100%); }
  .card-back .brand-name { left: 25px; top: 49px; font-size: 21px; color: #ffffff; }

  /* Compliment slip */
  .slip { left: 26px; top: 281px; width: 506px; height: 253px; }
  .slip .brand-dot { left: 42px; top: 20px; width: 54px; height: 54px; }
  .slip .brand-name { left: 27px; top: 86px; font-size: 18px; }
  .slip .tagline { left: 27px; top: 107px; font-size: 5.5px; }
  .slip .rule { position: absolute; left: 104px; top: 103px; width: 222px; height: 3px;
    background: linear-gradient(90deg, var(--teal), var(--lime)); }
  .slip .headline { position: absolute; left: 328px; top: 86px; font-size: 25px; font-weight: 400; color: var(--teal); white-space: nowrap; line-height: 1; }
  .slip .contact { left: 34px; top: 188px; font-size: 5px; }

  /* Envelope */
  .envelope { left: 24px; top: 550px; width: 506px; height: 253px; }
  .envelope .brand-dot { left: 48px; top: 18px; width: 54px; height: 54px; }
  .envelope .brand-name { left: 44px; top: 81px; font-size: 18px; }
  .envelope .tagline { left: 44px; top: 102px; font-size: 5.5px; }
  .envelope .return { position: absolute; left: 204px; top: 87px; font-size: 10px; font-weight: 300; color: var(--teal); line-height: 1.1; }
  .envelope .window { position: absolute; left: 45px; top: 123px; width: 207px; height: 103px;
    border: 1px solid var(--edge); border-radius: 12px; }
  .address { position: absolute; font-size: 9px; font-weight: 300; line-height: 1.3; color: var(--ink); }
  .address .att { font-weight: 400; margin-top: 9px; }
  .envelope .address { left: 38px; top: 32px; }

  /* Letterhead */
  .letterhead { left: 684px; top: 119px; width: 483px; height: 684px; }
  .letterhead .brand-dot { left: 84px; top: 54px; width: 50px; height: 50px; }
  .letterhead .brand-name { left: 78px; top: 113px; font-size: 16px; }
  .letterhead .tagline { left: 78px; top: 132px; font-size: 5px; }
  .letterhead .address { left: 78px; top: 174px; font-size: 8px; }
  .letter { position: absolute; left: 78px; top: 272px; width: 360px; font-size: 6.2px; font-weight: 300; line-height: 1.85; color: var(--ink); }
  .letter p { margin-bottom: 9px; }
  .letter .date { margin-bottom: 12px; }
  .letterhead .footer { position: absolute; top: 623px; font-size: 6px; font-weight: 400; color: var(--teal); line-height: 1.3; white-space: nowrap; }
</style>
</head>
<body>

  <section class="logo-main abs" style="left:0;top:0;width:210px;height:250px;">
    <div class="brand-dot" aria-hidden="true"></div>
    <div class="brand-name">TallCropNear</div>
    <div class="tagline">clear, crafted, focused communications</div>
  </section>

  <section class="sheet card-front">
    <div class="brand-dot" aria-hidden="true"></div>
    <div class="brand-name">TallCropNear</div>
    <div class="tagline">clear, crafted, focused communications</div>
    <div class="holder">Ellis Marsh</div>
    <div class="contact">
      <span class="light">14 Lintel Rd.</span><br>
      <span class="light">31400 Sydney</span><br>
      <span class="light">www.tallcropnear.com</span><br><br>
      T: +80 412 3456<br>
      M: +03 615 2020<br>
      <strong>ellis@tallcropnear.com</strong>
    </div>
  </section>

  <section class="sheet card-back">
    <div class="brand-name">TallCropNear</div>
  </section>

  <section class="sheet slip">
    <div class="brand-dot" aria-hidden="true"></div>
    <div class="brand-name">TallCropNear</div>
    <div class="tagline">clear, crafted, focused communications</div>
    <div class="rule"></div>
    <div class="headline">With Complements</div>
    <div class="contact">
      <span class="light">14 Lintel Rd.</span><br>
      <span class="light">31400 Sydney</span><br>
      <span class="light">www.tallcropnear.com</span><br><br>
      T: +80 412 3456<br>
      M: +03 615 2020<br>
      <strong>ellis@tallcropnear.com</strong>
    </div>
  </section>

  <section class="sheet envelope">
    <div class="brand-dot" aria-hidden="true"></div>
    <div class="brand-name">TallCropNear</div>
    <div class="tagline">clear, crafted, focused communications</div>
    <div class="return">14 Lintel Rd.<br>31400 Sydney</div>
    <div class="window">
      <div class="address">
        Kellaway Ltd.<br>82 Quarry Lane<br>31720 Sydney
        <div class="att">Att: Mrs. Penrow</div>
      </div>
    </div>
  </section>

  <section class="sheet letterhead">
    <div class="brand-dot" aria-hidden="true"></div>
    <div class="brand-name">TallCropNear</div>
    <div class="tagline">clear, crafted, focused communications</div>
    <div class="address">
      Kellaway Ltd.<br>82 Quarry Lane<br>31720 Sydney
      <div class="att">Att: Mrs. Penrow</div>
    </div>
    <div class="letter">
      <div class="date">April 19, 2011</div>
      <p>Concerning our last Meeting :</p>
      <p>Lorem ipsum dolor sit amet, consectetuer adipiscing elit. Pellentesque egeterat in nisl lobortis tempor. Maecenas tempor porta justo. Sed ligula risus, ullamcorper vel, volutpat sed, hendrerit vel, pede. Integer nisl. Sed sapienest, congue quis, mattis in, pulvinar ac, magna. Phasellus adipiscing odioat est. Nulla facilisi. Curabitur auctor leo non est. Aliquam non leo euarcu interdum tincidunt. Quisque eleifend dui dictum mauris.Nullam blandit,neque vel euismod tincidunt, massa mi adipiscing pede, ac gravida urna elitvitae risus.<br>In lacus mauris, suscipit et, consectetuer eget, euismod ac,magna. Nulla facilisi. Morbi adipiscing posuerevelit. Curabitur fringillacondimentum tortor. Mauris lacinia. Proin eget est. Nulla pulvinar facilisiserat. Donec vitae est at purus blandit vestibulum. Curabitur ante.</p>
      <p>Praesent dictum ipsum et turpis. Curabitur at diam. Morbi at dui. Vestibulumaugue magna, posuere at,scelerisque quis, vestibulum nec, dui. Nulla mattisjusto at ligula. Integer dui urna, scelerisque sit amet,nonummy ac,pellentesque id, nulla. Nulla vitae dolor. Ut rutrum, arcu sit amet luctusviverra, sapien orci luctus ipsum, id commodo risus ligula vitae ante. Sedornare diam et justo. Quisque iaculis quam id leo.Pellentesque laciniaellus sed leo. Nunc eget turpis vel quam fringilla tincidunt. Morbirhoncus, risus aporttitor vehicula, neque eros hendrerit urna, a gravid ametus massa ac arcu. Suspendisse eu metus. Duis necvelit ut nulla semper egestas.</p>
      <p>Best Regards,<br>Ellis Marsh</p>
    </div>
    <div class="footer" style="left:226px;">14 Lintel Rd.<br>31400 Sydney</div>
    <div class="footer" style="left:298px;">T: +80 412 3456<br>M: +03 615 2020</div>
    <div class="footer" style="left:370px;">ellis@tallcropnear.com<br>www.tallcropnear.com</div>
  </section>

</body>
</html>
```